Redesign of iOS App Lumo Tutor

Redesign of existing App Lumo Tutor, an app that helps learning Japanese Kanjis, Hiragana, Katakana.

The functionallity should remain the same as today: the app is free, you may download it at the app store. But: I like the design of my other apps better ;)

Target Market(s)

Students learning Japanese

Industry/Entity Type

Teacher

Font styles to use
Sans Serif

Requirements
Must have
• Lumo Tutor has 7 main screens, all screens has to be designed for iPhone and iPad: Main, Settings, Reading Tests, Writing Tests, Game, Paper Mode, Search
Nice to have
• I like the logo as it is today

```html
<!DOCTYPE html>
<html lang="en">
<head>
<meta charset="utf-8">
<title>Lumo Tutor – app screens</title>
<link href="https://fonts.googleapis.com/css2?family=Noto+Sans+JP:wght@300;400;500;700&family=Noto+Serif+JP:wght@700&display=swap" rel="stylesheet">
<style>
:root{
  --bg:#7d7d7d;
  --screen:#f3f3f3;
  --card:#ffffff;
  --ink:#1d1d1d;
  --muted:#9a9a9a;
  --faint:#d8d8d8;
  --line:#ececec;
  --green:#1fbf90;
  --blue:#3d8fea;
  --red:#f04e37;
  --yellow:#f0be1e;
  --slate:#7a7a7a;
  --seg:#e2e2e2;
}
*{box-sizing:border-box;margin:0;padding:0}
html,body{width:1183px;height:1200px;overflow:hidden}
body{background:var(--bg);font-family:"Noto Sans JP",sans-serif;color:var(--ink);position:relative}
.screen{position:absolute;width:213px;height:379px;background:var(--screen);overflow:hidden;box-shadow:0 6px 18px rgba(0,0,0,.25)}
.status{position:absolute;top:0;left:0;right:0;height:14px;background:#fff;font-size:6px;color:var(--muted);display:flex;justify-content:space-between;align-items:center;padding:0 6px}
.abs{position:absolute}
.center{position:absolute;transform:translateX(-50%);text-align:center;white-space:nowrap}
.hamburger{position:absolute;width:9px;height:7px;border-top:1px solid #999;border-bottom:1px solid #999}
.hamburger::after{content:"";position:absolute;left:0;right:0;top:2px;border-top:1px solid #999}
.bottombar{position:absolute;left:0;right:0;bottom:0;height:33px;background:var(--screen)}
.bottom-link{position:absolute;right:10px;top:13px;font-size:7px;font-weight:500;color:#444;letter-spacing:.3px}

/* main screen */
.tabs{position:absolute;top:14px;left:0;right:0;height:28px;background:#fff;display:flex;justify-content:space-around;align-items:center;padding:0 12px;font-size:7px;color:var(--muted)}
.tabs .active{color:var(--ink);font-weight:700;border-bottom:2px solid var(--slate);padding:0 4px 2px}
.tests{position:absolute;top:46px;left:0;right:0;height:300px;background:#fff}
.tests-head{position:absolute;top:8px;left:0;right:0;height:14px;font-size:6px;border-bottom:1px solid var(--line)}
.tests-head span{position:absolute}
.test-row{position:absolute;left:0;right:0;height:26px;border-bottom:1px solid var(--line);font-size:7px;font-weight:500}
.test-row .label{position:absolute;left:8px;top:8px}
.bar{position:absolute;top:7px;width:24px;height:12px;font-size:6px;color:#fff;text-align:right;padding-right:3px;line-height:12px;font-weight:700}
.b-total{left:104px;background:var(--slate)}
.b-ok{left:129px;background:var(--green)}
.b-mid{left:155px;background:var(--blue)}
.b-bad{left:181px;background:var(--red)}
.test-row.total .bar{background:none;text-align:center;font-weight:500}
.test-row.total .b-total{color:var(--slate)}
.test-row.total .b-ok{color:var(--green)}
.test-row.total .b-mid{color:var(--blue)}
.test-row.total .b-bad{color:var(--red)}
.tool{position:absolute;top:6px;transform:translateX(-50%);text-align:center;font-size:5px;color:var(--muted)}
.tool svg{display:block;margin:0 auto 2px}

/* score header */
.stat-label{position:absolute;top:33px;transform:translateX(-50%);font-size:7px;font-weight:700;letter-spacing:.3px}
.stat-value{position:absolute;top:42px;transform:translateX(-50%);font-size:14px;font-weight:300}
.stat-sub{position:absolute;top:61px;transform:translateX(-50%);font-size:6px;white-space:nowrap}
.is-green{color:var(--green)} .is-red{color:var(--red)} .is-blue{color:var(--blue)} .is-yellow{color:var(--yellow)}

.card{position:absolute;left:8px;width:197px;background:var(--card);box-shadow:0 1px 0 #e4e4e4,0 3px 0 #fff,0 4px 0 #e4e4e4,0 6px 0 #fff,0 7px 0 #e4e4e4}
.star{position:absolute;right:8px;top:8px}
.writing-grid{position:absolute;left:9px;top:60px;width:179px;height:178px;border:1px solid var(--line)}
.writing-grid::before{content:"";position:absolute;left:50%;top:0;bottom:0;border-left:1px solid var(--line)}
.writing-grid::after{content:"";position:absolute;top:50%;left:0;right:0;border-top:1px solid var(--line)}
.big-kanji{position:absolute;inset:0;display:flex;align-items:center;justify-content:center;font-family:"Noto Serif JP",serif;font-weight:700;font-size:150px;line-height:1;z-index:1}
.choice{position:absolute;width:32px;height:32px;border-radius:50%;border:2px solid;display:flex;align-items:center;justify-content:center;font-size:15px;background:#fff}

/* game */
.game-grid{position:absolute;left:9px;top:48px;display:grid;grid-template-columns:repeat(3,60px);grid-auto-rows:60px}
.game-grid div{display:flex;align-items:center;justify-content:center;font-size:14px;border-right:1px solid var(--line);border-bottom:1px solid var(--line)}
.game-grid div:nth-child(3n){border-right:none}
.game-grid div:nth-child(n+7){border-bottom:none}
.game-grid .dim{color:var(--faint)}
.coin{position:absolute;top:343px;width:32px;height:32px;border-radius:50%;border:2px solid var(--yellow);background:#fff;transform:translateX(-50%);display:flex;flex-direction:column;align-items:center;justify-content:center;font-size:5px;font-weight:700;line-height:1.2;text-align:center}
.coin small{font-size:4px;font-weight:400;color:var(--muted)}
.coin.off{border-color:#f6e1a0;color:#c8c8c8}

/* meaning grid */
.meaning-grid{position:absolute;left:8px;top:58px;display:grid;grid-template-columns:repeat(3,60px);grid-auto-rows:60px}
.meaning-grid div{display:flex;flex-direction:column;align-items:center;justify-content:center;font-size:8px;border-right:1px solid var(--line);border-bottom:1px solid var(--line);color:#333}
.meaning-grid div:nth-child(3n){border-right:none}
.meaning-grid div:nth-child(n+7){border-bottom:none}
.meaning-grid .wrong{background:var(--red);color:#fff;border-color:var(--red)}
.meaning-grid .right{background:var(--green);color:#fff;font-weight:700;border-color:var(--green)}

/* search */
.search{position:absolute;top:14px;left:0;right:0;height:41px;background:#fff}
.search-field{position:absolute;left:10px;right:10px;top:14px;height:17px;border-bottom:1px solid #ccc;font-size:8px;font-style:italic;color:#666;display:flex;align-items:center;gap:4px}
.entry{position:absolute;left:0;right:0;height:41px;background:#fff;border-bottom:1px solid var(--line)}
.entry .kana{position:absolute;left:10px;top:5px;font-size:20px;line-height:28px}
.entry .romaji{position:absolute;left:36px;top:7px;font-size:7px;line-height:8px}
.entry .dots{position:absolute;left:36px;top:22px;display:flex;gap:2px}
.entry .dots i{width:4px;height:4px;border-radius:50%;background:#c9c9c9}
.entry .type{position:absolute;left:76px;top:15px;font-size:8px}
.entry .lvl{position:absolute;left:177px;top:15px;font-size:8px}
.entry .star{right:8px;top:12px}

/* settings */
.settings-head{position:absolute;top:14px;left:0;right:0;height:29px;background:#fff;font-size:7px;color:#555;text-align:center;line-height:29px;letter-spacing:.3px}
.setting-label{position:absolute;left:10px;font-size:7.5px}
.segments{position:absolute;left:10px;right:10px;height:22px;display:flex;gap:2px}
.segments span{flex:1;background:var(--seg);color:#aaa;font-size:6px;font-weight:500;display:flex;align-items:center;justify-content:center;letter-spacing:.3px}
.segments .on{background:#fff;color:#111;font-weight:700}
.credits{position:absolute;top:362px;left:0;right:0;text-align:center;font-size:6px;font-style:italic;color:#777}
</style>
</head>
<body>

<!-- Main: test overview -->
<section class="screen" style="left:67px;top:130px">
  <div class="status"><span>●●●●○ Carrier</span><span>5:30PM</span><span>100% ▭</span></div>
  <nav class="tabs"><span>K</span><span class="active">N5</span><span>N4</span><span>N3</span><span>N2</span><span>N1</span><span>★</span></nav>
  <div class="tests">
    <div class="tests-head">
      <span style="left:8px;top:2px">TESTS</span>
      <span style="left:113px;top:1px;color:#888">▶</span>
      <span style="left:137px;top:0;color:var(--green);font-size:8px;font-weight:700">✓</span>
      <span style="left:164px;top:0;color:var(--blue);font-size:8px">○</span>
      <span style="left:190px;top:0;color:var(--red);font-size:8px">✕</span>
    </div>
    <div class="test-row" style="top:22px"><span class="label">Kanji ⇒ Meaning (103)</span><span class="bar b-total">103</span><span class="bar b-ok">0</span><span class="bar b-mid">0</span><span class="bar b-bad">0</span></div>
    <div class="test-row" style="top:48px"><span class="label">Meaning ⇒ Kanji (103)</span><span class="bar b-total">103</span><span class="bar b-ok">0</span><span class="bar b-mid">0</span><span class="bar b-bad">0</span></div>
    <div class="test-row" style="top:74px"><span class="label">Kanji ⇒ On (103)</span><span class="bar b-total">103</span><span class="bar b-ok">0</span><span class="bar b-mid">0</span><span class="bar b-bad">0</span></div>
    <div class="test-row" style="top:100px"><span class="label">On ⇒ Kanji (103)</span><span class="bar b-total">103</span><span class="bar b-ok">0</span><span class="bar b-mid">0</span><span class="bar b-bad">0</span></div>
    <div class="test-row" style="top:126px"><span class="label">Kanji ⇒ Kun (94)</span><span class="bar b-total">94</span><span class="bar b-ok">0</span><span class="bar b-mid">0</span><span class="bar b-bad">0</span></div>
    <div class="test-row" style="top:152px"><span class="label">Kun ⇒ Kanji (94)</span><span class="bar b-total">94</span><span class="bar b-ok">0</span><span class="bar b-mid">0</span><span class="bar b-bad">0</span></div>
    <div class="test-row" style="top:178px"><span class="label">Word ⇒ Reading (582)</span><span class="bar b-total">582</span><span class="bar b-ok">0</span><span class="bar b-mid">0</span><span class="bar b-bad">0</span></div>
    <div class="test-row" style="top:204px"><span class="label">Reading ⇒ Word (582)</span><span class="bar b-total">582</span><span class="bar b-ok">0</span><span class="bar b-mid">0</span><span class="bar b-bad">0</span></div>
    <div class="test-row" style="top:230px"><span class="label">Writing (103)</span><span class="bar b-total">103</span><span class="bar b-ok">0</span><span class="bar b-mid">0</span><span class="bar b-bad">0</span></div>
    <div class="test-row total" style="top:260px;border-bottom:none"><span class="label">ALL TESTS (1867)</span><span class="bar b-total">1867</span><span class="bar b-ok">0</span><span class="bar b-mid">0</span><span class="bar b-bad">0</span></div>
  </div>
  <div class="bottombar">
    <span class="hamburger" style="left:12px;top:13px"></span>
    <div class="tool" style="left:93px"><svg width="10" height="10" viewBox="0 0 10 10"><circle cx="5" cy="5" r="3.2" fill="none" stroke="#999" stroke-width="2" stroke-dasharray="1.6 1"/><circle cx="5" cy="5" r="1" fill="#999"/></svg>SETTINGS</div>
    <div class="tool" style="left:132px"><svg width="10" height="10" viewBox="0 0 10 10"><circle cx="5.5" cy="4" r="3" fill="none" stroke="#999" stroke-width="1.2"/><line x1="3.4" y1="6.2" x2="1" y2="9" stroke="#999" stroke-width="1.4"/></svg>SEARCH</div>
    <div class="tool" style="left:166px"><svg width="10" height="10" viewBox="0 0 10 10"><circle cx="5" cy="5" r="4" fill="none" stroke="#999" stroke-width="1"/><circle cx="5" cy="5" r="1.6" fill="#999"/></svg>GAMES</div>
    <div class="tool" style="left:196px"><svg width="10" height="10" viewBox="0 0 10 10"><path d="M2 1h4l2 2v6H2z" fill="#999"/></svg>PAPER</div>
  </div>
</section>

<!-- Reading test -->
<section class="screen" style="left:350px;top:130px">
  <div class="status"><span>●●●●○ Carrier</span><span>5:30PM</span><span>100% ▭</span></div>
  <span class="stat-label" style="left:42px">REMAINING</span><span class="stat-value" style="left:42px">102</span>
  <span class="stat-label is-green" style="left:106px">CORRECT</span><span class="stat-value is-green" style="left:106px">0</span>
  <span class="stat-label is-red" style="left:170px">WRONG</span><span class="stat-value is-red" style="left:170px">1</span>
  <div class="card" style="top:68px;height:254px">
    <svg class="star" width="10" height="10" viewBox="0 0 10 10"><path d="M5 .5l1.3 3 3.2.3-2.4 2.1.7 3.2L5 7.4 2.2 9.1l.7-3.2L.5 3.8l3.2-.3z" fill="none" stroke="#ccc" stroke-width=".7"/></svg>
    <div class="center" style="left:98px;top:10px;font-size:22px;font-weight:300">fire</div>
    <div class="center" style="left:98px;top:40px;font-size:7px;color:var(--muted)">カ、ひ</div>
    <div class="writing-grid"><div class="big-kanji">火</div></div>
  </div>
  <div class="bottombar">
    <span class="hamburger" style="left:10px;top:13px"></span>
    <span class="bottom-link">NEXT ›</span>
  </div>
</section>

<!-- Writing test -->
<section class="screen" style="left:632px;top:130px">
  <div class="status"><span>●●●●○ Carrier</span><span>5:30PM</span><span>100% ▭</span></div>
  <span class="stat-value is-blue" style="left:42px">0</span>
  <span class="stat-label is-green" style="left:106px">CORRECT</span><span class="stat-value is-green" style="left:106px">0</span>
  <span class="stat-label is-red" style="left:170px">WRONG</span><span class="stat-value is-red" style="left:170px">1</span>
  <div class="card" style="top:68px;height:254px">
    <div class="center is-green" style="left:98px;top:0;font-size:9px;font-weight:700">✓</div>
    <div class="center" style="left:98px;top:10px;font-size:24px;line-height:1.2">江</div>
    <div class="center" style="left:98px;top:42px;font-size:7px;color:var(--muted)">creek</div>
    <div class="writing-grid">
      <div class="big-kanji">江</div>
      <svg class="abs" style="right:6px;top:7px;z-index:2" width="8" height="10" viewBox="0 0 8 10"><path d="M0 1.5h8M3 .5h2M1 2.5l.6 7h4.8l.6-7" fill="none" stroke="#ccc" stroke-width="1"/></svg>
    </div>
  </div>
  <div class="bottombar">
    <span class="hamburger" style="left:10px;top:13px"></span>
  </div>
  <div class="choice" style="left:134px;top:342px;border-color:var(--green)">江</div>
  <div class="choice" style="left:171px;top:342px;border-color:var(--blue)">汢</div>
</section>

<!-- Game -->
<section class="screen" style="left:914px;top:130px">
  <div class="status"><span>●●●●○ Carrier</span><span>5:30PM</span><span>100% ▭</span></div>
  <span class="stat-label is-red" style="left:42px">LIVES</span><span class="stat-value is-red" style="left:42px">3</span><span class="stat-sub is-red" style="left:42px">Level N5</span>
  <span class="stat-label is-blue" style="left:106px">SCORE</span><span class="stat-value is-blue" style="left:106px">0</span><span class="stat-sub is-blue" style="left:106px">Highscore: 8</span>
  <span class="stat-label is-yellow" style="left:170px">COINS</span><span class="stat-value is-yellow" style="left:170px">12</span>
  <div class="card" style="top:76px;height:236px">
    <div class="center" style="left:98px;top:10px;font-size:21px;font-weight:300">ハク、びゃく</div>
    <div class="game-grid">
      <div class="dim">国</div><div class="dim">石</div><div>年</div>
      <div>七</div><div class="dim">外</div><div class="dim">毎</div>
      <div>一</div><div>百</div><div class="dim">新</div>
    </div>
  </div>
  <div class="bottombar"><span class="hamburger" style="left:10px;top:13px"></span></div>
  <div class="coin" style="left:79px">LEVEL<br>UP</div>
  <div class="coin off" style="left:115px">LIVE+<small>-24</small></div>
  <div class="coin" style="left:152px">SPLIT<small>-8</small></div>
  <div class="coin" style="left:189px">HINT<small>-4</small></div>
</section>

<!-- Meaning test -->
<section class="screen" style="left:210px;top:693px">
  <div class="status"><span>●●●●○ Carrier</span><span>5:30PM</span><span>100% ▭</span></div>
  <span class="stat-label" style="left:42px">REMAINING</span><span class="stat-value" style="left:42px">102</span>
  <span class="stat-label is-green" style="left:106px">CORRECT</span><span class="stat-value is-green" style="left:106px">0</span>
  <span class="stat-label is-red" style="left:170px">WRONG</span><span class="stat-value is-red" style="left:170px">1</span>
  <div class="card" style="top:68px;height:252px">
    <svg class="star" width="10" height="10" viewBox="0 0 10 10"><path d="M5 .5l1.3 3 3.2.3-2.4 2.1.7 3.2L5 7.4 2.2 9.1l.7-3.2L.5 3.8l3.2-.3z" fill="none" stroke="#ccc" stroke-width=".7"/></svg>
    <div class="center" style="left:98px;top:10px;font-size:26px;line-height:1.2">名</div>
    <div class="center" style="left:98px;top:42px;font-size:7px;color:var(--muted)">メイ、ミョウ、な</div>
    <div class="meaning-grid">
      <div>seven</div><div class="wrong"><b style="font-size:9px">✕</b>person</div><div>long</div>
      <div class="right"><b style="font-size:9px">✓</b>name</div><div>come</div><div>may</div>
      <div>write</div><div>in</div><div>station</div>
    </div>
  </div>
  <div class="bottombar">
    <span class="hamburger" style="left:10px;top:13px"></span>
    <span class="bottom-link" style="color:var(--muted)">SKIP ›</span>
  </div>
</section>

<!-- Search -->
<section class="screen" style="left:492px;top:693px">
  <div class="status"><span>●●●●○ Carrier</span><span>5:30PM</span><span>100% ▭</span></div>
  <div class="search"><div class="search-field"><svg width="9" height="9" viewBox="0 0 10 10"><circle cx="5.5" cy="4" r="3" fill="none" stroke="#555" stroke-width="1.2"/><line x1="3.4" y1="6.2" x2="1" y2="9" stroke="#555" stroke-width="1.4"/></svg>Search...</div></div>
  <div class="entry" style="top:58px"><span class="kana">あ</span><span class="romaji">a</span><span class="dots"><i></i><i></i><i></i></span><span class="type">Hiragana</span><span class="lvl">K</span><svg class="star" width="14" height="14" viewBox="0 0 10 10"><path d="M5 .5l1.3 3 3.2.3-2.4 2.1.7 3.2L5 7.4 2.2 9.1l.7-3.2L.5 3.8l3.2-.3z" fill="none" stroke="#ccc" stroke-width=".6"/></svg></div>
  <div class="entry" style="top:99px"><span class="kana">い</span><span class="romaji">i</span><span class="dots"><i></i><i></i><i></i></span><span class="type">Hiragana</span><span class="lvl">K</span><svg class="star" width="14" height="14" viewBox="0 0 10 10"><path d="M5 .5l1.3 3 3.2.3-2.4 2.1.7 3.2L5 7.4 2.2 9.1l.7-3.2L.5 3.8l3.2-.3z" fill="none" stroke="#ccc" stroke-width=".6"/></svg></div>
  <div class="entry" style="top:140px"><span class="kana">う</span><span class="romaji">u</span><span class="dots"><i></i><i></i><i></i></span><span class="type">Hiragana</span><span class="lvl">K</span><svg class="star" width="14" height="14" viewBox="0 0 10 10"><path d="M5 .5l1.3 3 3.2.3-2.4 2.1.7 3.2L5 7.4 2.2 9.1l.7-3.2L.5 3.8l3.2-.3z" fill="none" stroke="#ccc" stroke-width=".6"/></svg></div>
  <div class="entry" style="top:181px"><span class="kana">え</span><span class="romaji">e</span><span class="dots"><i></i><i></i><i></i></span><span class="type">Hiragana</span><span class="lvl">K</span><svg class="star" width="14" height="14" viewBox="0 0 10 10"><path d="M5 .5l1.3 3 3.2.3-2.4 2.1.7 3.2L5 7.4 2.2 9.1l.7-3.2L.5 3.8l3.2-.3z" fill="none" stroke="#ccc" stroke-width=".6"/></svg></div>
  <div class="entry" style="top:222px"><span class="kana">お</span><span class="romaji">o</span><span class="dots"><i></i><i></i><i></i></span><span class="type">Hiragana</span><span class="lvl">K</span><svg class="star" width="14" height="14" viewBox="0 0 10 10"><path d="M5 .5l1.3 3 3.2.3-2.4 2.1.7 3.2L5 7.4 2.2 9.1l.7-3.2L.5 3.8l3.2-.3z" fill="none" stroke="#ccc" stroke-width=".6"/></svg></div>
  <div class="entry" style="top:263px"><span class="kana">か</span><span class="romaji">ka</span><span class="dots"><i></i><i></i><i></i></span><span class="type">Hiragana</span><span class="lvl">K</span><svg class="star" width="14" height="14" viewBox="0 0 10 10"><path d="M5 .5l1.3 3 3.2.3-2.4 2.1.7 3.2L5 7.4 2.2 9.1l.7-3.2L.5 3.8l3.2-.3z" fill="none" stroke="#ccc" stroke-width=".6"/></svg></div>
  <div class="entry" style="top:304px"><span class="kana">が</span><span class="romaji">ga</span><span class="dots"><i></i><i></i><i></i></span><span class="type">Hiragana</span><span class="lvl">K</span><svg class="star" width="14" height="14" viewBox="0 0 10 10"><path d="M5 .5l1.3 3 3.2.3-2.4 2.1.7 3.2L5 7.4 2.2 9.1l.7-3.2L.5 3.8l3.2-.3z" fill="none" stroke="#ccc" stroke-width=".6"/></svg></div>
  <div class="bottombar">
    <span class="hamburger" style="left:10px;top:13px"></span>
    <span class="abs" style="left:28px;top:9px;font-size:9px;color:#999">?</span>
    <span class="bottom-link" style="font-weight:700">2278 ENTRIES FOUND ˄</span>
  </div>
</section>

<!-- Settings -->
<section class="screen" style="left:774px;top:693px;background:#ededed">
  <div class="status"><span>●●●●○ Carrier</span><span>5:30PM</span><span>100% ▭</span></div>
  <div class="settings-head">SETTINGS</div>
  <span class="hamburger" style="left:10px;top:26px"></span>

  <span class="setting-label" style="top:60px">Group Tests by:</span>
  <div class="segments" style="top:75px"><span class="on">NKT LEVEL</span><span>SCHOOL YEAR</span></div>

  <span class="setting-label" style="top:110px">Size of Answer Grid:</span>
  <div class="segments" style="top:124px"><span class="on">3 X 3</span><span>4 X 4</span></div>

  <span class="setting-label" style="top:159px">Show Meaning in Tests:</span>
  <div class="segments" style="top:174px"><span>NEVER</span><span class="on">CLASSIC</span><span>ALWAYS</span></div>

  <span class="setting-label" style="top:209px">Show Pattern in Writing Tests:</span>
  <div class="segments" style="top:223px"><span>NEVER</span><span class="on">FIRST TESTS</span><span>ALWAYS</span></div>

  <span class="setting-label" style="top:258px">Tests used in Game:</span>
  <div class="segments" style="top:272px"><span>MEANING</span><span>READING</span><span class="on">BOTH</span></div>

  <span class="setting-label" style="top:308px">Feedback:</span>
  <div class="segments" style="top:322px"><span>RATE</span><span>EMAIL</span></div>

  <p class="credits">many thanks to kotobadata.net and strokeset.hanmoji.org</p>
</section>

</body>
</html>
```